Auto Window Tinting for Local Business
Need Business card design
New card design

Target Market(s)

Local Audience
Repeat clients

Industry/Entity Type

Automotive Part

Contact Information for Business Card

Auto Window Tinting new crd design

Font styles to use
Serif

Colors

Designer to choose colors to be used in the design.

Requirements
Must have
• Facebook address
• IG address
• Phone Number
Nice to have
• Your own ideas
• Bold design
Should not have
• Auto graphics minimal
• Too many bright colors

```html
<!DOCTYPE html>
<html lang="en">
<head>
<meta charset="UTF-8">
<title>Summit Window Tinting – Business Card</title>
<link href="https://fonts.googleapis.com/css2?family=Roboto:wght@400;500;700;900&display=swap" rel="stylesheet">
<style>
  :root {
    --stage: #2b2b2b;
    --ink: #111111;
    --ink-soft: #444444;
    --muted: #9a9a9a;
    --paper: #ffffff;
    --silver-light: #e9e9e9;
    --silver-mid: #c4c4c4;
    --silver-dark: #a9a9a9;
    --rule: #d6d6d6;
  }
  * { box-sizing: border-box; margin: 0; padding: 0; }
  html, body { width: 1200px; height: 960px; overflow: hidden; }
  body {
    background: var(--stage);
    font-family: "Roboto", Arial, sans-serif;
    color: var(--ink);
    position: relative;
  }
  .card {
    position: absolute;
    width: 640px;
    height: 366px;
    box-shadow: 0 12px 30px rgba(0,0,0,.45);
  }
  .card--back {
    left: 90px; top: 90px;
    background: radial-gradient(ellipse at 40% 40%, var(--silver-light) 0%, var(--silver-mid) 60%, var(--silver-dark) 100%);
  }
  .card--front {
    left: 470px; top: 500px;
    background: var(--paper);
  }

  /* brand lockup */
  .brand { position: absolute; line-height: 1; }
  .brand__name {
    font-weight: 900;
    font-size: 44px;
    letter-spacing: 1px;
    text-transform: uppercase;
    color: var(--ink);
    display: flex; align-items: center; gap: 10px;
  }
  .brand__mark {
    width: 22px; height: 22px; border-radius: 50%;
    background: var(--ink);
    flex: none;
  }
  .brand__trade {
    font-weight: 900; font-size: 19px; letter-spacing: 3px;
    text-transform: uppercase; margin-top: 6px;
  }
  .brand__slogan { font-weight: 700; font-size: 17px; margin-top: 4px; }
  .brand__phone { font-weight: 900; font-size: 34px; margin-top: 4px; letter-spacing: 1px; }

  /* back */
  .card--back .brand { left: 44px; top: 110px; }
  .benefits {
    position: absolute; left: 370px; top: 96px;
    list-style: none; font-size: 17px; color: var(--ink);
  }
  .benefits li { display: flex; align-items: center; gap: 8px; margin-bottom: 6px; }
  .benefits svg { width: 16px; height: 16px; flex: none; }
  .promise {
    position: absolute; left: 0; right: 0; bottom: 40px;
    display: flex; align-items: center; justify-content: center; gap: 12px;
    font-weight: 900; font-size: 14px; letter-spacing: 2px; text-transform: uppercase;
  }
  .promise::before, .promise::after {
    content: ""; width: 38px; height: 2px; background: var(--ink);
  }

  /* front */
  .card--front .brand { left: 40px; top: 110px; }
  .divider {
    position: absolute; left: 372px; top: 40px; bottom: 40px;
    width: 1px; background: linear-gradient(var(--paper), var(--rule) 20%, var(--rule) 80%, var(--paper));
  }
  .contact { position: absolute; left: 400px; top: 100px; }
  .contact__name { font-weight: 700; font-size: 24px; letter-spacing: 1px; text-transform: uppercase; }
  .contact__role { font-size: 15px; color: var(--muted); text-transform: uppercase; margin-top: 2px; letter-spacing: 1px; }
  .contact__list { list-style: none; margin-top: 18px; }
  .contact__list li {
    display: flex; align-items: center; gap: 8px;
    font-size: 14.5px; color: var(--ink-soft); margin-bottom: 6px;
  }
  .contact__icon { width: 14px; height: 14px; flex: none; }
</style>
</head>
<body>

<section class="card card--back" aria-label="Card back">
  <div class="brand">
    <div class="brand__name"><span class="brand__mark"></span>Summit</div>
    <div class="brand__trade">Window Tinting</div>
    <div class="brand__slogan">Don't squint, window TINT!</div>
    <div class="brand__phone">555-014-2290</div>
  </div>
  <ul class="benefits">
    <li><svg viewBox="0 0 16 16"><rect x="1" y="3" width="12" height="12" fill="none" stroke="#111" stroke-width="1.5"/><path d="M3 8l4 4 8-11" fill="none" stroke="#111" stroke-width="2.2"/></svg>Block Unwanted Heat</li>
    <li><svg viewBox="0 0 16 16"><rect x="1" y="3" width="12" height="12" fill="none" stroke="#111" stroke-width="1.5"/><path d="M3 8l4 4 8-11" fill="none" stroke="#111" stroke-width="2.2"/></svg>Protect Skin From UV Rays</li>
    <li><svg viewBox="0 0 16 16"><rect x="1" y="3" width="12" height="12" fill="none" stroke="#111" stroke-width="1.5"/><path d="M3 8l4 4 8-11" fill="none" stroke="#111" stroke-width="2.2"/></svg>Protect Interior From Fading</li>
    <li><svg viewBox="0 0 16 16"><rect x="1" y="3" width="12" height="12" fill="none" stroke="#111" stroke-width="1.5"/><path d="M3 8l4 4 8-11" fill="none" stroke="#111" stroke-width="2.2"/></svg>Improve Overall Appearance</li>
  </ul>
  <div class="promise">Mobile Service - Lifetime Warranty</div>
</section>

<section class="card card--front" aria-label="Card front">
  <div class="brand">
    <div class="brand__name"><span class="brand__mark"></span>Summit</div>
    <div class="brand__trade">Window Tinting</div>
    <div class="brand__slogan">Don't squint, window TINT!</div>
    <div class="brand__phone">555-014-2290</div>
  </div>
  <div class="divider"></div>
  <div class="contact">
    <div class="contact__name">Marcus Delane</div>
    <div class="contact__role">Owner</div>
    <ul class="contact__list">
      <li><svg class="contact__icon" viewBox="0 0 14 14"><rect x="1" y="3" width="12" height="8" fill="#111"/><path d="M1 3l6 5 6-5" fill="none" stroke="#fff" stroke-width="1.2"/></svg>summit_tint@mailbox.example</li>
      <li><svg class="contact__icon" viewBox="0 0 14 14"><circle cx="7" cy="7" r="6" fill="#111"/></svg>social.example/summitwindow</li>
      <li><svg class="contact__icon" viewBox="0 0 14 14"><circle cx="7" cy="7" r="6" fill="#111"/></svg>@summit_windowtinting</li>
    </ul>
  </div>
</section>

</body>
</html>
```